The Brightwater Compass Business Card

We need an attractive business card with the logo that we bought from ArtVantly last year.
Our mission is to contribute to change the way today's leaders manage business companies bringing value to the workplace and helping them to build a new model of creating wealth.
Our logo is clear about our values : we seek Positive Change through People and are convinced that the pursuit of individual well-being and the chase of economic results can converge with the right management.
Management Consulting
Corinne Fabrelle
+34 612 98 70 31
corinne.fabrelle@thebrightwatercompass-mail.net
www.thebrightwatercompass-mail.net

```html
<!DOCTYPE html>
<html lang="en">
<head>
<meta charset="utf-8">
<title>The Brightwater Compass – Business Card</title>
<link rel="stylesheet" href="https://fonts.googleapis.com/css2?family=Poppins:wght@400;600&display=swap">
<style>
  :root {
    --page-bg: #e7e7e7;
    --card-teal: #00877f;
    --card-teal-light: #00938b;
    --card-teal-dark: #007a73;
    --ink-white: #ffffff;
  }
  * { margin: 0; padding: 0; box-sizing: border-box; }
  html, body {
    width: 1200px;
    height: 900px;
    overflow: hidden;
    background: var(--page-bg);
    font-family: "Poppins", sans-serif;
  }
  .canvas {
    position: relative;
    width: 1200px;
    height: 900px;
  }
  .card {
    position: absolute;
    left: 290px;
    width: 620px;
    height: 354px;
    background: radial-gradient(ellipse at 40% 35%, var(--card-teal-light), var(--card-teal) 55%, var(--card-teal-dark));
    color: var(--ink-white);
    box-shadow: 0 4px 14px rgba(0, 0, 0, 0.18);
    display: flex;
    flex-direction: column;
    align-items: center;
    justify-content: center;
  }
  .card--front { top: 76px; }
  .card--back { top: 470px; }

  .brand {
    display: flex;
    align-items: center;
    gap: 16px;
  }
  .brand__dot {
    width: 34px;
    height: 34px;
    border-radius: 50%;
    background: var(--ink-white);
  }
  .brand__name {
    font-weight: 600;
    font-size: 34px;
    letter-spacing: 0.04em;
    text-transform: uppercase;
  }

  .contact {
    text-align: center;
    font-weight: 400;
    font-size: 14px;
    letter-spacing: 0.12em;
    line-height: 1.55;
  }
  .contact__name {
    font-weight: 600;
    letter-spacing: 0.14em;
  }
</style>
</head>
<body>
<main class="canvas">
  <section class="card card--front" aria-label="Business card front">
    <div class="brand">
      <span class="brand__dot"></span>
      <span class="brand__name">The Brightwater Compass</span>
    </div>
  </section>

  <section class="card card--back" aria-label="Business card back">
    <address class="contact" style="font-style: normal;">
      <div class="contact__name">Corinne Fabrelle</div>
      <div class="contact__phone">+34 612 98 70 31</div>
      <div class="contact__email">corinne.fabrelle@thebrightwatercompass-mail.net</div>
      <div class="contact__web">www.thebrightwatercompass-mail.net</div>
    </address>
  </section>
</main>
</body>
</html>
```